Thornbury Fields Enterprise
Home grown grain fed beef Wholes, Halfs, Quarters
Locally raised
No Added Hormones
Call or text now to order (555) -0193-7720

```html
<!DOCTYPE html>
<html lang="en">
<head>
<meta charset="UTF-8">
<title>Thornbury Fields Enterprise – Homegrown Grain-Fed Beef</title>
<link rel="stylesheet" href="https://fonts.googleapis.com/css2?family=Poppins:wght@500;600;700;800&display=swap">
<style>
  :root {
    --bg-deep: #010a04;
    --bg-green: #0a7a35;
    --bg-mid: #03351a;
    --accent: #8dc63f;
    --white: #ffffff;
    --card-white: #ffffff;
    --meat-red: #bf3b40;
    --meat-deep: #a62c34;
    --meat-fat: #f3e6e0;
  }
  * { margin: 0; padding: 0; box-sizing: border-box; }
  html, body { width: 927px; height: 1200px; overflow: hidden; background: var(--bg-deep); }
  body { font-family: "Poppins", sans-serif; color: var(--white); }

  .flyer {
    position: relative;
    width: 927px;
    height: 1200px;
    overflow: hidden;
    background:
      radial-gradient(ellipse 520px 560px at 60px 120px, rgba(14,140,60,0.95), rgba(6,90,38,0.6) 45%, transparent 80%),
      radial-gradient(ellipse 600px 420px at 200px 560px, rgba(8,100,42,0.75), transparent 75%),
      linear-gradient(160deg, var(--bg-green) 0%, var(--bg-mid) 35%, var(--bg-deep) 70%, #000 100%);
  }

  .leaf-decor {
    position: absolute;
    border-radius: 60% 10% 60% 10%;
    filter: blur(3px);
  }
  .leaf-decor--top { left: -30px; top: -20px; width: 170px; height: 90px; transform: rotate(25deg);
    background: radial-gradient(ellipse at 40% 40%, #8fd07a, #3f8f3a 70%, transparent 100%); opacity: .8; }
  .leaf-decor--bottom { right: -30px; bottom: -30px; width: 250px; height: 150px; transform: rotate(-20deg);
    background: radial-gradient(ellipse at 45% 45%, #86d075, #3c8f38 70%, transparent 100%); opacity: .85; }

  .dot-column { position: absolute; display: flex; flex-direction: column; gap: 20px; }
  .dot-column span { width: 6px; height: 6px; background: #1f8a62; display: block; }
  .dot-column--top { left: 878px; top: 85px; }
  .dot-column--mid { left: 329px; top: 962px; }
  .dot-column--mid span { background: #0e4a2a; }

  .brand { position: absolute; left: 0; top: 98px; width: 927px; text-align: center; }
  .brand__name { font-weight: 700; font-size: 74px; line-height: 1; letter-spacing: 1px; }
  .brand__tag { margin-top: 14px; font-weight: 600; font-size: 54px; line-height: 1; letter-spacing: 16px; padding-left: 16px; }
  .brand__rule { position: absolute; left: 298px; top: 164px; width: 330px; height: 3px; background: var(--white); }

  .headline { position: absolute; left: 40px; top: 356px; font-weight: 700; line-height: 1; }
  .headline__line { display: block; font-size: 67px; letter-spacing: 0.5px; }
  .headline__line + .headline__line { margin-top: -2px; }
  .headline__beef { display: block; font-size: 124px; color: var(--accent); font-weight: 800; margin-top: -6px; margin-left: 4px; letter-spacing: 1px; }
  .headline__rule { position: absolute; left: 49px; top: 601px; width: 255px; height: 7px; background: var(--accent); }

  .portions { position: absolute; left: 40px; top: 622px; list-style: none; font-weight: 700; font-size: 32px; line-height: 38px; letter-spacing: 0.5px; }

  .features { position: absolute; left: 40px; top: 762px; list-style: none; font-weight: 500; font-size: 22px; }
  .features li { display: flex; align-items: center; height: 37px; }
  .features li::before { content: ""; width: 18px; height: 18px; border-radius: 3px; background: var(--accent); margin-right: 16px; }

  .promise { position: absolute; left: 40px; top: 880px; }
  .promise__lead { font-weight: 700; font-size: 38px; color: var(--accent); line-height: 1.1; letter-spacing: 0.5px; }
  .promise__sub { font-weight: 500; font-size: 22px; line-height: 1.2; }

  .order { position: absolute; left: 40px; top: 1035px; width: 440px; height: 116px; border: 1.5px solid var(--accent); border-radius: 30px; padding: 18px 0 0 30px; }
  .order__label { font-weight: 600; font-size: 26px; line-height: 1.3; }
  .order__phone { font-weight: 700; font-size: 40px; line-height: 1.15; color: var(--accent); letter-spacing: 0.5px; }

  .product-card { position: absolute; left: 494px; top: 298px; width: 391px; height: 707px; background: var(--card-white); border-radius: 44px; overflow: hidden; }
  .product-card__frame { position: absolute; inset: 13px; border: 2.5px solid var(--accent); border-radius: 34px; }
  .product-card__shadow { position: absolute; left: 36px; top: 620px; width: 330px; height: 22px; border-radius: 50%;
    background: radial-gradient(ellipse, rgba(0,0,0,.55), rgba(0,0,0,0) 70%); }
  .product-card__photo { position: absolute; left: 20px; top: 205px; width: 351px; height: 380px; border-radius: 50%;
    background: radial-gradient(ellipse 50% 50% at 50% 50%, var(--meat-red) 0%, var(--meat-deep) 55%, var(--meat-fat) 80%, rgba(255,255,255,0) 100%); }
</style>
</head>
<body>
<main class="flyer">
  <div class="leaf-decor leaf-decor--top" role="img" aria-label="Fresh green herb leaves"></div>
  <div class="leaf-decor leaf-decor--bottom" role="img" aria-label="Fresh green herb leaves"></div>

  <div class="dot-column dot-column--top"><span></span><span></span><span></span><span></span></div>

  <header class="brand">
    <h1 class="brand__name">THORNBURY FIELDS</h1>
    <p class="brand__tag">ENTERPRISE</p>
    <div class="brand__rule"></div>
  </header>

  <h2 class="headline">
    <span class="headline__line">HOMEGROW</span>
    <span class="headline__line">GRAIN-FED</span>
    <span class="headline__beef">BEEF</span>
  </h2>
  <div class="headline__rule"></div>

  <ul class="portions">
    <li>WHOLES</li>
    <li>HALVES</li>
    <li>QUARTERS AVAILABLE</li>
  </ul>

  <ul class="features">
    <li>Locally Raised</li>
    <li>No Added Hormones</li>
  </ul>

  <div class="promise">
    <p class="promise__lead">Fresh, Natural,</p>
    <p class="promise__sub">and Premium Quality Beef.</p>
  </div>

  <div class="dot-column dot-column--mid"><span></span><span></span><span></span></div>

  <section class="order">
    <p class="order__label">Call or Text Now to Order:</p>
    <p class="order__phone">(555) 0193-7720</p>
  </section>

  <div class="product-card">
    <div class="product-card__frame"></div>
    <div class="product-card__photo" role="img" aria-label="Two raw beef steaks with fresh sage and rosemary sprigs"></div>
    <div class="product-card__shadow"></div>
  </div>
</main>
</body>
</html>
```